Tamarind Shore Insurance (TSI

Project Brief for TSI Insurance Website Redesign

Background:
TSI is a leading insurance company based in the Caribbean, offering a wide range of insurance products and services. We aim to redesign our website to reflect a modern, user-friendly, and vibrant online presence that resonates with our diverse Caribbean clientele, particularly reflecting the African American and Caribbean demographic.

Objective:
To create a modern, engaging, and informative website that effectively communicates TSI's insurance products and services to current and potential clients, with a focus on lifestyle-oriented imagery and content.

Target Audience:
Our primary audience includes individuals, families, and businesses in the Caribbean, especially those looking for reliable and comprehensive insurance solutions. The design should appeal to a diverse range of ages but should be particularly attractive to middle-aged professionals.

Design Requirements:

Modern, clean, and user-friendly interface.
Vibrant and lifestyle-oriented imagery and graphics, featuring people of African American or Caribbean ethnicity to reflect our client base.
Mobile-responsive design to ensure accessibility on all devices.
Intuitive navigation and layout to enhance user experience.
Website Pages:
The website should include the following pages:

Home
Whole Life Insurance
Health Insurance
Motor Insurance
Group Insurance
Health Claim
About Us
Agents
Forms
Get a Quote
Investor Relations
Insurance Education
Set an Appointment
Contact Us
Additional Pages/Suggestions:

Testimonials: showcasing customer reviews and stories.
FAQs: addressing common questions about insurance policies and processes.
Careers: highlighting employment opportunities and promoting TSI as a great place to work.
News and Updates: featuring the latest news, updates, and tips related to insurance and lifestyle.
Accessibility Features: ensuring the site is accessible to users with disabilities.
Design Options:
We would like to receive at least two design options to choose from, each presenting a different look and feel while adhering to the design requirements outlined above.

Imagery and Content:

Use high-quality, authentic images that represent the diverse lifestyles of our Caribbean audience.
Ensure that content is clear, concise, and easy to understand, avoiding insurance jargon where possible.
Highlight key products and services clearly on the homepage to direct users effectively.
Functionality Requirements:

SEO optimized to enhance visibility on search engines.
Fast loading times to improve user experience and reduce bounce rates.
Secure online forms for quotes, appointments, and claims submissions.
Integration with social media platforms to enhance engagement and reach.
Submission Guidelines:

Proposals should include detailed design mockups for key pages.
Outline the proposed user journey and experience.
Provide an estimated timeline and budget for the project.
Include case studies or examples of previous work, particularly in the insurance or financial services sectors.
Evaluation Criteria:

Creativity and originality of the design.
Alignment with TSI’s brand and target audience.
User experience and site navigation.
Technical feasibility and scalability.
Cost-effectiveness and adherence to budget and timeline.
Deadline for Submission:
March 4, 2024

ALSO I have attached some brand assets to assist.

Target Market(s)

Companies, Car Owners, Home Builders, Groups wanting Health Insurance, Private and Business

Industry/Entity Type

Insurance

Number of Pages Required

5+ page

Font styles to use
Sans Serif

Colors
00AB8E
00BBA5
67D7C9
C6EFE9
E9F9F6
FFF300
FFF600
FEFA6F
FFFEC7
FFFEE8
EB3D1F
EC4F4E
F09395
F8D3D4
FCEDEE

Requirements
Must have
• Provided Logo, African American people
Nice to have
• They should ask
Should not have
• No other ethnicity but African American

```html
<!DOCTYPE html>
<html lang="en">
<head>
<meta charset="utf-8">
<title>Tamarind Shore Insurance</title>
<link rel="stylesheet" href="https://fonts.googleapis.com/css2?family=Outfit:wght@300;400;500;600;700;800;900&display=swap">
<style>
:root{
  --green:#3ab54a;
  --green-dark:#2e9a3d;
  --green-light:#8fdc93;
  --black:#0b0b0b;
  --ink:#1c1c1c;
  --body:#3a3a3a;
  --muted:#6b6b6b;
  --paper:#ffffff;
  --mist:#f4f4f6;
  --sand:#efebe6;
  --star:#f7a21b;
}
*{box-sizing:border-box;margin:0;padding:0}
html,body{width:1200px;height:3886px;overflow:hidden}
body{font-family:"Outfit",sans-serif;color:var(--ink);background:var(--paper);position:relative}
.abs{position:absolute}
a{color:inherit;text-decoration:none}

/* top bar */
.topbar{left:0;top:0;width:1200px;height:33px;background:var(--green)}
.topbar .link{top:0;height:33px;display:flex;align-items:center;gap:8px;justify-content:center;color:#fff;font-size:11px}
.topbar .edu{left:777px;width:166px;background:var(--green-dark)}
.topbar .inv{left:943px;width:147px;background:var(--black)}
.topbar .dot{width:10px;height:10px;border-radius:50%;background:#fff}
.topbar .notch{left:116px;top:22px;width:0;height:0;border-left:14px solid transparent;border-right:14px solid transparent;border-bottom:11px solid #fff}

/* header */
.header{left:0;top:33px;width:1200px;height:67px;background:#fff}
.brand{display:flex;align-items:center;gap:9px}
.brand .mark{width:30px;height:30px;border-radius:50%;background:var(--green);flex:none}
.brand .name{font-weight:700;color:var(--green);font-size:15px;line-height:1.05;letter-spacing:.5px;text-transform:uppercase}
.header .brand{position:absolute;left:109px;top:14px}
.nav{position:absolute;left:410px;top:0;height:67px;display:flex;align-items:center;gap:28px;font-size:10.5px;font-weight:500;text-transform:uppercase}
.quote{position:absolute;left:990px;top:16px;width:100px;height:34px;border:1.5px solid var(--ink);border-radius:17px;font-size:10.5px;font-weight:600;display:flex;align-items:center;justify-content:center}

/* hero */
.hero{left:0;top:100px;width:1200px;height:600px;background:var(--sand);overflow:hidden}
.hero-photo{left:640px;top:0;width:560px;height:600px;background:linear-gradient(120deg,var(--sand) 0%,#cfc3b5 30%,#6b4a36 60%,#3a2a22 100%)}
.eyebrow{left:109px;top:212px;font-size:17px;font-weight:400}
.hero-title{left:109px;top:245px;font-size:47px;font-weight:900;line-height:1.15;letter-spacing:.3px}
.hero-text{left:109px;top:366px;width:460px;font-size:14px;line-height:1.5;color:var(--body)}
.btn-green{background:var(--green);color:#fff;border-radius:22px;font-size:11px;font-weight:500;display:flex;align-items:center;justify-content:center;text-transform:uppercase}
.hero .btn-green{left:109px;top:330px;width:192px;height:42px}
.wave{left:0;width:1200px}

/* section heads */
.h-split{font-size:46px;letter-spacing:-.5px;text-transform:uppercase}
.h-split b{font-weight:700}
.h-split span{font-weight:300}
.divider{display:flex;align-items:center;gap:8px}
.divider i{display:block;width:22px;height:2px;background:var(--green)}
.divider em{display:block;width:13px;height:13px;border-radius:50%;background:var(--green-dark);border:2px solid var(--green-light)}
.para{font-size:13px;line-height:1.65;color:var(--body)}
.btn-dark{background:var(--black);color:#fff;border-radius:18px;font-size:11px;font-weight:500;display:flex;align-items:center;justify-content:center;text-transform:uppercase}

/* about */
.about-grey{left:330px;top:778px;width:200px;height:200px;border-radius:50%;background:#ececec}
.about-black{left:150px;top:1040px;width:100px;height:100px;border-radius:50%;background:var(--black)}
.about-frame{left:128px;top:755px;width:345px;height:400px;border:6px solid var(--green);border-radius:40px 40px 172px 172px;background:#fff;padding:12px;box-shadow:0 14px 30px rgba(0,0,0,.12)}
.about-frame .ph{width:100%;height:100%;border-radius:30px 30px 160px 160px;background:linear-gradient(160deg,#7a8b96,#3d3430 55%,#d8d3cc)}
.about-title{left:645px;top:800px}
.about-div{left:643px;top:862px}
.about-text{left:645px;top:900px;width:445px}
.about-btn{left:645px;top:1075px;width:132px;height:36px}

/* services */
.services{left:0;top:1262px;width:1200px;height:670px;background:linear-gradient(180deg,#ededed,#fafafa 60%,#fff)}
.svc-title{left:0;top:1332px;width:1200px;text-align:center}
.svc-div{left:563px;top:1396px}
.card{top:1425px;width:233px;height:414px;background:#fff;box-shadow:0 2px 10px rgba(0,0,0,.08);text-align:center}
.card .ph{position:absolute;left:6px;top:6px;width:221px;height:172px}
.card .ico{position:absolute;left:89px;top:150px;width:56px;height:56px;border-radius:50%;background:var(--green);border:4px solid #fff;display:flex;align-items:center;justify-content:center}
.card h3{position:absolute;left:0;top:225px;width:100%;font-size:16px;font-weight:700;text-transform:uppercase}
.card p{position:absolute;left:20px;top:255px;width:193px;font-size:11.5px;line-height:1.45;color:var(--body)}
.card .more{position:absolute;left:56px;top:347px;width:121px;height:32px;border:1.5px solid var(--green);border-radius:16px;font-size:9.5px;font-weight:600;display:flex;align-items:center;justify-content:center;text-transform:uppercase}
.card.active{background:var(--green);color:#fff}
.card.active p{color:#fff}
.card.active .more{background:#fff;color:var(--ink);border-color:#fff}
.card.active .ico{border-color:var(--green);background:#fff}

/* banner */
.banner{left:0;top:1932px;width:1200px;height:400px;background:linear-gradient(180deg,#1a1714,#0c0b0a)}
.banner-sub{left:0;top:2005px;width:1200px;text-align:center;color:#fff;font-size:49px;font-weight:300}
.banner-title{left:0;top:2068px;width:1200px;text-align:center;color:#fff;font-size:49px;font-weight:900;text-transform:uppercase}
.banner .btn-green{}

/* learning */
.learning{left:0;top:2330px;width:1200px;height:622px;background:var(--mist)}
.learn-grey{left:623px;top:2805px;width:150px;height:150px;border-radius:50%;background:#e6e6e6}
.learn-black{left:968px;top:2600px;width:92px;height:92px;border-radius:50%;background:var(--black)}
.learn-frame{left:630px;top:2450px;width:260px;height:350px;border:5px solid var(--green);border-radius:30px 30px 130px 130px}
.learn-photo{left:680px;top:2395px;width:320px;height:557px;border-radius:160px 160px 0 0;background:linear-gradient(180deg,#2a211c 0%,#5c3a24 22%,#a0612f 50%,#e8e2d8 85%)}
.learn-title{left:109px;top:2522px}
.learn-div{left:109px;top:2584px}
.learn-text{left:109px;top:2622px;width:450px}
.learn-btn{left:110px;top:2799px;width:121px;height:36px}

/* testimonials */
.tst-title{left:0;top:3036px;width:1200px;text-align:center}
.tst-div{left:563px;top:3100px}
.review{top:3152px;width:296px;height:272px;background:#fff;box-shadow:0 2px 14px rgba(0,0,0,.09)}
.review .av{position:absolute;left:22px;top:36px;width:54px;height:54px;border-radius:50%;border:3px solid var(--green);background:linear-gradient(160deg,#c9b6a3,#5a3f30)}
.review .who{position:absolute;left:86px;top:42px;font-size:14px;font-weight:600}
.review .stars{position:absolute;left:86px;top:62px;color:var(--star);font-size:14px;letter-spacing:1px}
.review p{position:absolute;left:22px;top:110px;width:250px;font-size:11.5px;line-height:1.75;color:var(--body)}
.review .q{position:absolute;right:18px;bottom:8px;font-size:96px;line-height:1;font-weight:900;color:#e3e3e3;height:60px;overflow:hidden}

/* footer */
.footer{left:0;top:3590px;width:1200px;height:296px;background:var(--black);color:#fff}
.footer .brand{position:absolute;left:114px;top:60px}
.social{position:absolute;left:128px;top:112px;display:flex;gap:12px}
.social span{width:40px;height:40px;border-radius:50%;background:#3b3b3b;display:block}
.social span:first-child{background:var(--green)}
.fcol{position:absolute;top:64px;font-size:12px}
.fcol h4{font-size:11.5px;font-weight:500;margin-bottom:12px;text-transform:uppercase}
.fcol li{list-style:none;line-height:19px;color:#ddd}
.news{position:absolute;left:817px;top:87px;width:270px;height:40px;border-radius:20px;background:#3a3a3a;color:#aaa;font-size:12px;display:flex;align-items:center;padding-left:30px}
.news .go{position:absolute;right:4px;top:3px;width:34px;height:34px;border-radius:50%;background:var(--green)}
.fine{position:absolute;left:822px;top:140px;width:270px;font-size:8.5px;line-height:1.5;color:#bbb}
.rule{position:absolute;left:106px;top:226px;width:982px;height:2px;background:#333}
.copy{position:absolute;left:0;top:252px;width:1200px;text-align:center;font-size:12px;color:#ccc}
</style>
</head>
<body>

<div class="abs topbar">
  <div class="abs notch"></div>
  <a class="abs link edu" href="#"><span class="dot"></span>Insurance Education</a>
  <a class="abs link inv" href="#"><span class="dot"></span>Investor Relations</a>
</div>

<header class="abs header">
  <div class="brand"><span class="mark"></span><span class="name">Tamarind Shore<br>Insurance</span></div>
  <nav class="nav">
    <a href="#">Home</a><a href="#">About Us</a><a href="#">Insurance Service ▾</a><a href="#">Health Claim</a><a href="#">Agents</a><a href="#">FAQ's</a><a href="#">Contact Us</a>
  </nav>
  <a class="quote" href="#">GET A QUOTE</a>
</header>

<section class="abs hero">
  <div class="abs hero-photo" role="img" aria-label="Smiling family with a young child gathered around a laptop at home"></div>
  <p class="abs eyebrow" style="top:112px">TAMARIND SHORE INSURANCE</p>
  <h1 class="abs hero-title" style="top:145px">ALWAYS HERE<br>FOR YOU...ALWAYS</h1>
  <p class="abs hero-text" style="top:265px">Insurance Company Based In The Caribbean, Offering A Wide Range Of Insurance Products And Services.</p>
  <a class="abs btn-green" href="#">Set An Appointment</a>
</section>
<svg class="abs wave" style="top:615px" width="1200" height="90" viewBox="0 0 1200 90" preserveAspectRatio="none">
  <path d="M0 80 C200 20 330 5 470 20 C620 36 760 60 900 40 C1030 22 1120 20 1200 40 L1200 90 L0 90Z" fill="#fff"/>
  <path d="M0 78 C200 18 330 2 470 17 C620 33 760 58 900 38 C1030 20 1120 18 1200 38 L1200 60 C1120 40 1030 42 900 60 C760 80 620 56 470 40 C330 26 200 40 0 84Z" fill="var(--green-light)"/>
  <path d="M0 76 C200 14 330 -2 470 13 C620 29 760 52 900 32 C1030 14 1120 12 1200 30 L1200 42 C1120 26 1030 28 900 46 C760 66 620 42 470 28 C330 14 200 28 0 82Z" fill="var(--green)"/>
</svg>

<!-- about -->
<div class="abs about-grey"></div>
<div class="abs about-black"></div>
<div class="abs about-frame"><div class="ph" role="img" aria-label="Smiling woman in glasses working at a desk with a laptop"></div></div>
<h2 class="abs h-split about-title"><b>ABOUT</b> <span>US</span></h2>
<div class="abs divider about-div"><i></i><em></em></div>
<p class="abs para about-text">Lorem ipsum dolor sit amet, consectetur adipiscing elit. In vel porta ex. Interdum et malesuada fames ac ante ipsum primis in faucibus. Aenean sollicitudin nulla pellentesque, sodales sapien quis, bibendum tortor. Fusce ullamcorper diam sed justo dictum, sit amet laoreet massa faucibus. Integer ac eleifend turpis. Vestibulum fermentum dignissim sapien sit amet imperdiet. Quisque ultricies leo sapien, a bibendum mauris mollis vel.</p>
<a class="abs btn-dark about-btn" href="#">Learn More</a>

<!-- services -->
<section class="abs services"></section>
<h2 class="abs h-split svc-title"><b>OUR SERVICE</b> <span>INSURANCE</span></h2>
<div class="abs divider svc-div"><i></i><em></em><i></i></div>

<article class="abs card" style="left:110px">
  <div class="ph" role="img" aria-label="Family talking with an advisor in a living room" style="background:linear-gradient(150deg,#d8cbb8,#6e5442 60%,#3b2c24)"></div>
  <div class="ico"><svg width="24" height="24" viewBox="0 0 24 24" fill="none" stroke="#fff" stroke-width="2.4" stroke-linecap="round" stroke-linejoin="round"><path d="M5 12.5l4.5 4.5L19 7"/></svg></div>
  <h3>Whole Life Insurance</h3>
  <p>Lorem ipsum dolor sit amet, consectetur adipiscing elit. In vel porta ex. Interdum et malesuada fames ac ante ipsum primis</p>
  <a class="more" href="#">Learn More</a>
</article>
<article class="abs card active" style="left:359px">
  <div class="ph" role="img" aria-label="Doctor examining a young child sitting on a parent's lap" style="background:linear-gradient(150deg,#b9d6d2,#3f9c8c 45%,#3a2b26)"></div>
  <div class="ico"><svg width="24" height="24" viewBox="0 0 24 24" fill="none" stroke="#3ab54a" stroke-width="3" stroke-linecap="round"><path d="M12 5v14M5 12h14"/></svg></div>
  <h3>Health Insurance</h3>
  <p>Lorem ipsum dolor sit amet, consectetur adipiscing elit. In vel porta ex. Interdum et malesuada fames ac ante ipsum primis</p>
  <a class="more" href="#">Learn More</a>
</article>
<article class="abs card" style="left:608px">
  <div class="ph" role="img" aria-label="Couple receiving car keys from a dealer" style="background:linear-gradient(150deg,#c8c8c4,#5b4a40 55%,#2d2520)"></div>
  <div class="ico"><svg width="26" height="26" viewBox="0 0 24 24" fill="none" stroke="#fff" stroke-width="2" stroke-linejoin="round"><path d="M4 15v-3l2-5h12l2 5v3z"/><circle cx="8" cy="16" r="1.8"/><circle cx="16" cy="16" r="1.8"/></svg></div>
  <h3>Motor Insurance</h3>
  <p>Lorem ipsum dolor sit amet, consectetur adipiscing elit. In vel porta ex. Interdum et malesuada fames ac ante ipsum primis</p>
  <a class="more" href="#">Learn More</a>
</article>
<article class="abs card" style="left:858px">
  <div class="ph" role="img" aria-label="Group of colleagues reviewing documents together" style="background:linear-gradient(150deg,#9a9a9a,#4a3a32 55%,#1f1a17)"></div>
  <div class="ico"><svg width="26" height="26" viewBox="0 0 24 24" fill="none" stroke="#fff" stroke-width="2"><circle cx="8.5" cy="8" r="3"/><circle cx="15.5" cy="8" r="3"/><path d="M3 19c0-3 2.5-5 5.5-5s5.5 2 5.5 5M11 19c0-3 2-5 4.5-5S21 16 21 19"/></svg></div>
  <h3>Group Insurance</h3>
  <p>Lorem ipsum dolor sit amet, consectetur adipiscing elit. In vel porta ex. Interdum et malesuada fames ac ante ipsum primis</p>
  <a class="more" href="#">Learn More</a>
</article>

<!-- banner -->
<section class="abs banner" role="img" aria-label="Darkened photo of a family gathering"></section>
<p class="abs banner-sub">Tamarind Shore Insurance</p>
<h2 class="abs banner-title">ALWAYS HERE FOR YOU...ALWAYS</h2>
<a class="abs btn-green" href="#" style="left:504px;top:2151px;width:192px;height:41px">Set An Appointment</a>

<!-- learning -->
<section class="abs learning"></section>
<svg class="abs wave" style="top:2260px" width="1200" height="100" viewBox="0 0 1200 100" preserveAspectRatio="none">
  <path d="M0 0 H1200 V10 C1100 20 1000 40 900 30 C760 14 620 10 450 30 C300 48 160 60 0 40Z" fill="#0c0b0a"/>
  <path d="M0 20 C160 40 300 28 450 12 C620 -6 760 0 900 18 C1000 30 1100 10 1200 -2 L1200 30 C1100 40 1000 64 900 56 C760 44 620 36 450 52 C300 66 160 80 0 48Z" fill="var(--green)"/>
  <path d="M0 44 C160 74 300 62 450 46 C620 30 760 38 900 52 C1000 60 1100 36 1200 26 L1200 40 C1100 52 1000 76 900 70 C760 60 620 52 450 66 C300 80 160 90 0 56Z" fill="var(--green-light)"/>
</svg>
<div class="abs learn-grey"></div>
<div class="abs learn-frame"></div>
<div class="abs learn-black"></div>
<div class="abs learn-photo" role="img" aria-label="Laughing young woman with curly hair pointing at herself"></div>
<h2 class="abs h-split learn-title"><b>LEARNING</b> <span>CENTER</span></h2>
<div class="abs divider learn-div"><em></em><i></i></div>
<p class="abs para learn-text">Lorem ipsum dolor sit amet, consectetur adipiscing elit. In vel porta ex. Interdum et malesuada fames ac ante ipsum primis in faucibus. Aenean sollicitudin nulla pellentesque, sodales sapien quis, bibendum tortor. Fusce ullamcorper diam sed justo dictum, sit amet laoreet massa faucibus. Integer ac eleifend turpis. Vestibulum fermentum dignissim sapien sit amet imperdiet. Quisque ultricies leo sapien, a bibendum mauris mollis vel.</p>
<a class="abs btn-dark learn-btn" href="#">Enter</a>

<!-- testimonials -->
<h2 class="abs h-split tst-title"><b>WHAT OUR CLIENTS</b> <span>SAY ABOUT US</span></h2>
<div class="abs divider tst-div"><i></i><em></em><i></i></div>

<article class="abs review" style="left:110px">
  <div class="av" role="img" aria-label="Client portrait"></div>
  <p class="who">Keisha Morant</p><p class="stars">★★★★★</p>
  <p>"Lorem ipsum dolor sit amet, cnsectetuar adipiscing elit. Mauris sagittis faucibusas mauris eget tincidunt. Proin fermentum it nisl eros, vel fermentum libero molestieas quis. Proin tincidunt sit amits"</p>
  <span class="q">“</span>
</article>
<article class="abs review" style="left:452px">
  <div class="av" role="img" aria-label="Client portrait"></div>
  <p class="who">Dorian Pryce</p><p class="stars">★★★★★</p>
  <p>"Lorem ipsum dolor sit amet, cnsectetuar adipiscing elit. Mauris sagittis faucibusas mauris eget tincidunt. Proin fermentum it nisl eros, vel fermentum libero molestieas quis. Proin tincidunt sit amits"</p>
  <span class="q">“</span>
</article>
<article class="abs review" style="left:794px">
  <div class="av" role="img" aria-label="Client portrait"></div>
  <p class="who">Dorian Pryce</p><p class="stars">★★★★★</p>
  <p>"Lorem ipsum dolor sit amet, cnsectetuar adipiscing elit. Mauris sagittis faucibusas mauris eget tincidunt. Proin fermentum it nisl eros, vel fermentum libero molestieas quis. Proin tincidunt sit amits"</p>
  <span class="q">“</span>
</article>

<!-- footer -->
<svg class="abs wave" style="top:3510px" width="1200" height="85" viewBox="0 0 1200 85" preserveAspectRatio="none">
  <path d="M0 70 C150 40 300 30 450 34 C650 40 800 10 950 8 C1060 6 1140 20 1200 34 L1200 85 L0 85Z" fill="var(--black)"/>
  <path d="M0 66 C150 30 300 18 450 22 C650 28 800 0 950 0 C1060 0 1140 12 1200 24 L1200 40 C1140 26 1060 14 950 16 C800 18 650 44 450 40 C300 36 150 46 0 72Z" fill="var(--green)"/>
  <path d="M0 70 C150 40 300 30 450 34 C650 38 800 14 950 12 C1060 10 1140 24 1200 34 L1200 42 C1140 30 1060 20 950 22 C800 24 650 48 450 46 C300 42 150 50 0 76Z" fill="var(--green-light)"/>
</svg>
<footer class="abs footer">
  <div class="brand"><span class="mark"></span><span class="name">Tamarind Shore<br>Insurance</span></div>
  <div class="social"><span></span><span></span><span></span><span></span></div>
  <div class="fcol" style="left:382px"><h4>Learn More</h4><ul><li>Home</li><li>About Us</li><li>Insurance Service</li></ul></div>
  <div class="fcol" style="left:527px"><h4>About Us</h4><ul><li>Health Claim</li><li>Agents</li><li>Faq's</li><li>Contact Us</li></ul></div>
  <div class="fcol" style="left:672px"><h4>Support</h4><ul><li>User Terms</li><li>Privacy</li><li>Ftc Disclosure</li><li>Kit</li></ul></div>
  <div class="fcol" style="left:820px"><h4>Newsletter</h4></div>
  <div class="news">Email<span class="go"></span></div>
  <p class="fine">By using this form you agree with the storage and handling of your data by Tidewell. Read our privacy policy.</p>
  <div class="rule"></div>
  <p class="copy">©2024tamarindshoreinsurance.com All Rights Reserved</p>
</footer>

</body>
</html>
```